Retail healthy snack bar design

We are launching a new product range to be sold in health food stores.

The Fennick Co (no logo as yet).

We will have a range of bars, spreads (jars), shakes (bags) in the following ranges-
milk protein
plant protein
keto

For this project, please do a bar design. The chosen designer will be given additional work for the rest of the packaging as well as promotional material such as social media, banners, posters etc.

Lumo Bar Protein - Must be White to be recognized.
Lumo Bar Collagen - Bronze
Lumo Keto Bar - Possibly Red
Lumo Bar Plant - Green

Food images can be added but their must be samples without as we may need to remove for certain countries.

Target Market(s)

Healthy, Weight-loss, Bodybuilding, Elderly, Medical

Industry/Entity Type

Health And Wellness

Font styles to use
Sans Serif

Colors

Designer to choose colors to be used in the design.

Requirements
Must have
• Clean simple to read design with minimal colours

Flavour to be easily read (Must include the word 'Flavour' in the same size font as the flavour description)

Must show size of bar (60g).

Some details that can be added (optional)-
raw, cold pressed bar with (example) whey protein isolate + prebiotic fibre
natural, with no artificial colours, flavours, preservatives or sweeteners
no added sugar or sugar alcohols - gluten free - soy free

Rear of bar shall remain the same or all same details if redesigned.
Nice to have
• Clean design, use of silver foil and/or matt/gloss affect, large oversized flavour image (if including).

See images of current designs I like on the market for ideas
Should not have
• Too many images (if any).

```html
<!DOCTYPE html>
<html lang="en">
<head>
<meta charset="utf-8">
<title>Lumo Bar Protein – Vanilla Wrapper</title>
<link rel="stylesheet" href="https://fonts.googleapis.com/css2?family=Open+Sans:ital,wght@0,400;0,700;0,800;1,800&display=swap">
<style>
  :root {
    --stage: #282828;
    --wrap-bright: #1c40f2;
    --wrap-mid: #1230c8;
    --wrap-deep: #08087a;
    --band: #2f52f6;
    --band-edge: #020a5e;
    --flavour: #ffe20a;
    --ink: #111111;
    --white: #ffffff;
    --muted: #b9c0e6;
  }
  * { margin: 0; padding: 0; box-sizing: border-box; }
  html, body {
    width: 1200px; height: 857px; overflow: hidden;
    background: var(--stage);
    font-family: "Open Sans", Arial, sans-serif;
  }
  .canvas { position: relative; width: 1200px; height: 857px; }
  .wrapper-art { position: absolute; inset: 0; }
  .brand-name {
    position: absolute; left: 318px; top: 352px;
    font-weight: 800; font-size: 86px; line-height: 1;
    color: var(--white); letter-spacing: -1px;
  }
  .flavour {
    position: absolute; left: 800px; top: 288px; width: 140px;
    text-align: right;
    font-weight: 800; font-style: italic; font-size: 25px; line-height: 1.25;
    color: var(--ink);
  }
  .weight {
    position: absolute; left: 837px; top: 489px;
    width: 74px; height: 74px; border-radius: 50%;
    background: var(--white);
    display: flex; align-items: center; justify-content: center;
    font-size: 27px; font-weight: 400; color: var(--ink);
  }
  .weight small { font-size: 17px; margin-top: 8px; }
  .claim {
    position: absolute; left: 296px; top: 532px;
    font-size: 17px; color: var(--muted);
  }
</style>
</head>
<body>
<main class="canvas">
  <svg class="wrapper-art" width="1200" height="857" viewBox="0 0 1200 857">
    <defs>
      <linearGradient id="wrap-fill" x1="0" y1="0" x2="1" y2="0">
        <stop offset="0" stop-color="var(--wrap-bright)"/>
        <stop offset="0.45" stop-color="var(--wrap-mid)"/>
        <stop offset="0.7" stop-color="var(--wrap-deep)"/>
        <stop offset="1" stop-color="var(--wrap-deep)"/>
      </linearGradient>
      <clipPath id="wrap-shape">
        <polygon points="200,274 1000,274 1014,290 1000,305 1014,320 1000,335 1014,350 1000,365 1014,380 1000,395 1014,410 1000,425 1014,440 1000,455 1014,470 1000,485 1014,500 1000,515 1014,530 1000,545 1014,560 1000,571 200,571 183,560 198,545 183,530 198,515 183,500 198,485 183,470 198,455 183,440 198,425 183,410 198,395 183,380 198,365 183,350 198,335 183,320 198,305 183,290"/>
      </clipPath>
      <path id="band-curve" d="M415,505 Q585,462 745,492"/>
    </defs>

    <g class="wrapper" clip-path="url(#wrap-shape)">
      <rect class="wrapper-base" x="180" y="270" width="840" height="310" fill="url(#wrap-fill)"
            role="img" aria-label="Abstract blue branch-line background pattern"/>
      <circle class="flavour-disc" cx="903" cy="297" r="114" fill="var(--flavour)"/>
    </g>

    <g class="name-band">
      <path d="M380,472 Q585,425 788,445 L755,522 Q585,482 405,524 Z"
            fill="var(--band)" stroke="var(--band-edge)" stroke-width="4" stroke-linejoin="round"/>
      <text font-family="Open Sans, Arial, sans-serif" font-weight="700" font-size="36"
            fill="var(--white)" letter-spacing="17">
        <textPath href="#band-curve">PROTEIN</textPath>
      </text>
    </g>
  </svg>

  <div class="brand-name">Lumo Bar</div>
  <p class="flavour">VANILA<br>FLAVOUR</p>
  <div class="weight">60<small>g</small></div>
  <p class="claim">no added sugar</p>
</main>
</body>
</html>
```